Business Card Design for Mabel's Pantry

We make food for dogs.
Business Card Design (using the logo designed by you). Our Brand color is a bright canary yellow. For example our signage is predominantly yellow, with the logo in black. I'd like the card also to use that imagery.
Feel free to use the two sides creatively.
Vertical Design is also great.

Industry/Entity Type

Pet food

Contact Information for Business Card

Name, email, website, phone no

Font styles to use
Sans Serif

Colors
59FF00
82FF00
B8FF75
E3FFCB
F4FFEA
FFF300
FFF600
FEFA6F
FFFEC7
FFFEE8

Requirements
Nice to have
• A graphic in the same brush stroke style of the logo shoeing a doggy bowl of food

```html
<!DOCTYPE html>
<html lang="en">
<head>
<meta charset="utf-8">
<title>Mabel's Pantry — Business Card</title>
<link rel="stylesheet" href="https://fonts.googleapis.com/css2?family=Montserrat:wght@400;500;700;800&display=swap">
<style>
  :root {
    --bg: #d9d9dc;
    --card: #2a2a2b;
    --card-deep: #222223;
    --pattern-a: #2f2f30;
    --pattern-b: #1c1c1d;
    --canary: #fff000;
    --text: #ffffff;
  }
  * { box-sizing: border-box; margin: 0; padding: 0; }
  html, body { width: 1200px; height: 900px; overflow: hidden; }
  body {
    background: var(--bg);
    font-family: "Montserrat", Arial, sans-serif;
    display: flex;
    flex-direction: column;
    align-items: center;
    justify-content: center;
    gap: 40px;
  }
  .card {
    width: 700px;
    height: 400px;
    border-radius: 22px;
    background: var(--card);
    position: relative;
    overflow: hidden;
  }
  .card--front { border-bottom: 8px solid var(--canary); }
  .brand {
    position: absolute;
    left: 60px;
    top: 0;
    bottom: 0;
    width: 300px;
    display: flex;
    align-items: center;
    gap: 12px;
  }
  .brand__dot {
    width: 16px; height: 16px;
    border-radius: 50%;
    background: var(--canary);
    flex: none;
  }
  .brand__name {
    color: var(--canary);
    font-weight: 700;
    font-size: 34px;
    letter-spacing: 1px;
    text-transform: uppercase;
    line-height: 1;
  }
  .divider {
    position: absolute;
    left: 385px;
    top: 90px;
    width: 1px;
    height: 210px;
    background: var(--canary);
    opacity: .8;
  }
  .contact {
    position: absolute;
    left: 415px;
    top: 92px;
    color: var(--text);
  }
  .contact__name {
    color: var(--canary);
    font-weight: 800;
    font-size: 24px;
    letter-spacing: 2px;
    text-transform: uppercase;
  }
  .contact__title { font-size: 15px; margin: 2px 0 18px; }
  .contact__address { font-size: 15px; line-height: 1.4; margin-bottom: 16px; }
  .contact__list { list-style: none; font-size: 15px; line-height: 1.7; }
  .contact__list li { display: flex; align-items: center; gap: 10px; }
  .contact__icon { width: 14px; height: 14px; flex: none; }
  .card--back { background: var(--card-deep); }
  .back__pattern {
    position: absolute; inset: 0;
    background: linear-gradient(135deg, var(--pattern-a), var(--pattern-b) 60%, var(--pattern-a));
  }
  .back__brand {
    position: absolute;
    right: 70px;
    bottom: 60px;
    display: flex;
    align-items: center;
    gap: 10px;
  }
  .back__brand .brand__name { font-size: 22px; }
  .back__brand .brand__dot { width: 12px; height: 12px; }
</style>
</head>
<body>
  <section class="card card--front" aria-label="Card front">
    <div class="brand">
      <span class="brand__dot"></span>
      <span class="brand__name">Mabel's Pantry</span>
    </div>
    <div class="divider"></div>
    <div class="contact">
      <p class="contact__name">Daniel Ressler</p>
      <p class="contact__title">Founder/CEO</p>
      <p class="contact__address">2150 Orchard Lane Name<br>Brookfield AB 3092</p>
      <ul class="contact__list">
        <li>
          <svg class="contact__icon" viewBox="0 0 14 14"><path d="M3 1l2.5 3-1.5 1.5a7 7 0 0 0 4.5 4.5L10 8.5l3 2.5-1.5 2A11 11 0 0 1 1 2.5z" fill="var(--canary)"/></svg>
          (555)-214-3096
        </li>
        <li>
          <svg class="contact__icon" viewBox="0 0 14 14"><rect x="1" y="3" width="12" height="8" fill="var(--canary)"/><path d="M1 3l6 5 6-5" fill="none" stroke="var(--card)" stroke-width="1.2"/></svg>
          info@mabelspantry.com
        </li>
        <li>
          <svg class="contact__icon" viewBox="0 0 14 14"><circle cx="7" cy="7" r="6" fill="none" stroke="var(--canary)" stroke-width="1.4"/><ellipse cx="7" cy="7" rx="2.5" ry="6" fill="none" stroke="var(--canary)" stroke-width="1.2"/><path d="M1 7h12" stroke="var(--canary)" stroke-width="1.2"/></svg>
          www.mabelspantry.com
        </li>
      </ul>
    </div>
  </section>

  <section class="card card--back" aria-label="Card back">
    <div class="back__pattern" role="img" aria-label="Tone-on-tone repeating brand mark pattern"></div>
    <div class="back__brand">
      <span class="brand__dot"></span>
      <span class="brand__name">Mabel's Pantry</span>
    </div>
  </section>
</body>
</html>
```